Menu Design Project for an Italian cafe

Casual Italian style cafe situated in Chinatown in Sydney Australia . Value for money food, good coffee and good location are the cafes strengths. Catering to bushiness crowd in the morning/lunch, tourist crowd for brunch and Asian customers for late afternoon coffee.
Design concept is understated, casual European chic. Should communicate a casual escape to have a good meet up with friends to escape the hustle and bustle of the city crowd.
Would like to move away from current colors of dark brown, creme, black and orange. Would like a more enticing vibrant and brighter colour scheme.
Industry/Entity Type
Cafe
Look and feel
Each slider illustrates characteristics of the customer's brand and the style your logo design should communicate.

```html
<!DOCTYPE html>
<html lang="en">
<head>
<meta charset="utf-8">
<title>Tavola Cafe Restaurant – Menu</title>
<link href="https://fonts.googleapis.com/css2?family=Alfa+Slab+One&family=Comfortaa:wght@400;700&family=Courgette&family=Lobster+Two:ital,wght@1,700&family=Open+Sans:wght@400;600&family=Rye&display=swap" rel="stylesheet">
<style>
  :root{
    --teal:#3ba384;
    --teal-deep:#2f8a6e;
    --lime:#d5d34a;
    --lime-light:#dedc5c;
    --charcoal:#554d4a;
    --charcoal-dark:#4a4341;
    --sun:#f3c431;
    --brick:#7e2118;
    --brick-soft:#8e2c1e;
    --cream:#f5ebc4;
    --white:#ffffff;
  }
  *{margin:0;padding:0;box-sizing:border-box}
  html,body{width:933px;height:1200px;overflow:hidden;background:var(--teal)}
  .menu{position:relative;width:933px;height:1200px;background:radial-gradient(ellipse at 50% 40%,#44ad8d 0%,var(--teal) 60%,var(--teal-deep) 100%)}
  .sheet{position:absolute;left:45px;top:45px;width:843px;height:1110px;background:radial-gradient(ellipse at 40% 50%,var(--lime-light) 0%,var(--lime) 70%,#c9c744 100%)}
  .masthead{position:absolute;left:57px;top:60px;width:816px;height:247px;background:var(--charcoal)}
  .welcome{position:absolute;left:433px;top:84px;width:66px;height:66px;border-radius:50%;background:var(--sun);display:flex;align-items:center;justify-content:center;font:12px 'Courgette',cursive;color:var(--brick)}
  .brand{position:absolute;left:315px;top:142px;width:306px;height:80px;background:var(--teal);display:flex;flex-direction:column;align-items:center;justify-content:center;color:var(--white)}
  .brand-name{font:700 36px/1 'Comfortaa',sans-serif;display:flex;align-items:center;gap:10px}
  .brand-name::before{content:"";width:22px;height:22px;border-radius:50%;border:2px solid var(--white)}
  .brand-tag{font:700 11px 'Comfortaa',sans-serif;letter-spacing:1px;margin-top:4px;padding-left:34px;color:var(--white)}
  .address,.phone{position:absolute;left:57px;width:816px;text-align:center;color:var(--white);font:700 16px 'Comfortaa',sans-serif}
  .address{top:245px}
  .phone{top:270px}

  .kicker{position:absolute;width:300px;text-align:center;font:600 7px 'Open Sans',sans-serif;letter-spacing:1.5px;color:var(--cream);text-transform:uppercase}
  .section-band{position:absolute;left:150px;width:285px;height:32px;background:var(--sun);opacity:.9}
  .section-title{position:absolute;width:400px;text-align:center;font:30px/1 'Rye',serif;color:var(--brick)}
  .subhead{position:absolute;width:260px;text-align:center;font:italic 700 19px 'Lobster Two',cursive;color:var(--teal-deep);transform:translateX(-50%)}
  .rule{position:absolute;left:68px;width:532px;border-top:2px dotted rgba(255,255,255,.55)}

  .item{position:absolute;width:270px;transform:translateX(-50%);text-align:center}
  .item-name{font:12px/1 'Alfa Slab One',serif;color:var(--brick-soft);text-transform:uppercase;letter-spacing:.3px}
  .item-desc{margin-top:5px;font:600 7.5px/1.35 'Open Sans',sans-serif;color:var(--teal-deep);text-transform:uppercase;letter-spacing:.3px}

  .dish{position:absolute;border-radius:50%;background:var(--cream);box-shadow:0 0 0 4px rgba(245,235,196,.5)}
  .dish .photo{position:absolute;inset:9px;border-radius:50%}

  .specials{position:absolute;left:608px;top:322px;width:262px;height:833px;background:var(--charcoal-dark)}
  .specials-band{position:absolute;left:638px;top:348px;width:202px;height:40px;background:var(--teal)}
  .specials-title{position:absolute;left:608px;top:352px;width:262px;text-align:center;font:32px/1 'Rye',serif;color:var(--cream);letter-spacing:1px}
  .special-name{position:absolute;left:608px;width:262px;text-align:center;font:600 15px 'Open Sans',sans-serif;color:var(--white)}
  .special-desc{position:absolute;left:630px;width:218px;text-align:center;font:400 8.5px/1.3 'Open Sans',sans-serif;color:var(--white)}
  .price{position:absolute;width:66px;height:66px;border-radius:50%;background:var(--brick-soft);border:3px solid var(--cream);display:flex;align-items:center;justify-content:center;font:22px 'Rye',serif;color:var(--white)}
</style>
</head>
<body>
<main class="menu">
  <div class="sheet"></div>

  <header>
    <div class="masthead"></div>
    <div class="welcome">Welcome</div>
    <div class="brand">
      <div class="brand-name">Tavola</div>
      <div class="brand-tag">CAFE RESTAURANT</div>
    </div>
    <p class="address">48 Lantern Lane Shop 5-6 Harbour Arcade, Sydney, NSW 2000</p>
    <p class="phone">02 9000 4812</p>
  </header>

  <!-- Starters -->
  <div class="kicker" style="left:143px;top:325px">Only from organic ingredients</div>
  <div class="section-band" style="top:335px"></div>
  <h2 class="section-title" style="left:93px;top:336px">STARTERS</h2>
  <div class="subhead" style="left:192px;top:368px">Salads</div>
  <div class="subhead" style="left:465px;top:368px">Appetizers</div>
  <div class="rule" style="top:398px"></div>

  <div class="item" style="left:185px;top:411px"><div class="item-name">Agricento Salad - $5</div><div class="item-desc">Lorem ipsum dolor sit amet, consectetur adipiscing<br>elit. Morbi egestas lacinia dolor eget elementum</div></div>
  <div class="item" style="left:185px;top:464px"><div class="item-name">Caesar Salad - $5</div><div class="item-desc">Lorem ipsum dolor sit amet, consectetur adipiscing<br>elit. Morbi egestas lacinia dolor eget elementum</div></div>
  <div class="item" style="left:185px;top:517px"><div class="item-name">Caprese - $5</div><div class="item-desc">Lorem ipsum dolor sit amet, consectetur adipiscing<br>elit. Morbi egestas lacinia dolor eget elementum</div></div>
  <div class="item" style="left:185px;top:570px"><div class="item-name">Garden Salad - $5</div><div class="item-desc">Lorem ipsum dolor sit amet, consectetur adipiscing<br>elit. Morbi egestas lacinia dolor eget elementum</div></div>
  <div class="item" style="left:185px;top:623px"><div class="item-name">Greek Salad - $5</div><div class="item-desc">Lorem ipsum dolor sit amet, consectetur adipiscing<br>elit. Morbi egestas lacinia dolor eget elementum</div></div>

  <div class="item" style="left:465px;top:411px"><div class="item-name">Glazed Carrots - $5</div><div class="item-desc">Lorem ipsum dolor sit amet, consectetur adipiscing<br>elit. Morbi egestas lacinia dolor eget elementum</div></div>
  <div class="item" style="left:465px;top:464px"><div class="item-name">Zucchini Sticks - $5</div><div class="item-desc">Lorem ipsum dolor sit amet, consectetur adipiscing<br>elit. Morbi egestas lacinia dolor eget elementum</div></div>
  <div class="item" style="left:465px;top:517px"><div class="item-name">Stuffed Snow Peas - $5</div><div class="item-desc">Lorem ipsum dolor sit amet, consectetur adipiscing<br>elit. Morbi egestas lacinia dolor eget elementum</div></div>
  <div class="item" style="left:465px;top:570px"><div class="item-name">Seaweed - $5</div><div class="item-desc">Lorem ipsum dolor sit amet, consectetur adipiscing<br>elit. Morbi egestas lacinia dolor eget elementum</div></div>
  <div class="item" style="left:465px;top:623px"><div class="item-name">Pakoras - $5</div><div class="item-desc">Lorem ipsum dolor sit amet, consectetur adipiscing<br>elit. Morbi egestas lacinia dolor eget elementum</div></div>

  <div class="dish" style="left:86px;top:684px;width:140px;height:140px"><div class="photo" role="img" aria-label="Photo of a grain salad with toasted bread and a coffee cup" style="background:radial-gradient(circle,#8a6a3e,#5a4230)"></div></div>
  <div class="dish" style="left:260px;top:684px;width:140px;height:140px"><div class="photo" role="img" aria-label="Photo of a topped bruschetta plate" style="background:radial-gradient(circle,#c98a5a,#8a5a38)"></div></div>
  <div class="dish" style="left:438px;top:684px;width:140px;height:140px"><div class="photo" role="img" aria-label="Photo of a fresh green salad with tomatoes" style="background:radial-gradient(circle,#7aa24a,#4f7a32)"></div></div>

  <!-- Beverages -->
  <div class="kicker" style="left:143px;top:841px">Only from organic ingredients</div>
  <div class="section-band" style="top:850px"></div>
  <h2 class="section-title" style="left:93px;top:851px">BEVERAGES</h2>
  <div class="subhead" style="left:189px;top:882px">Cocktails</div>
  <div class="subhead" style="left:465px;top:882px">Hot and Cold Drinks</div>
  <div class="rule" style="top:911px"></div>

  <div class="item" style="left:185px;top:926px"><div class="item-name">Blue Hawaii - $5</div><div class="item-desc">Lorem ipsum dolor sit amet, consectetur adipiscing<br>elit. Morbi egestas lacinia dolor eget elementum</div></div>
  <div class="item" style="left:185px;top:980px"><div class="item-name">Caipirinha - $5</div><div class="item-desc">Lorem ipsum dolor sit amet, consectetur adipiscing<br>elit. Morbi egestas lacinia dolor eget elementum</div></div>
  <div class="item" style="left:185px;top:1033px"><div class="item-name">Havana Cooler - $5</div><div class="item-desc">Lorem ipsum dolor sit amet, consectetur adipiscing<br>elit. Morbi egestas lacinia dolor eget elementum</div></div>
  <div class="item" style="left:185px;top:1086px"><div class="item-name">Blue Hawaii - $5</div><div class="item-desc">Lorem ipsum dolor sit amet, consectetur adipiscing<br>elit. Morbi egestas lacinia dolor eget elementum</div></div>

  <div class="item" style="left:465px;top:925px"><div class="item-name">Black Tea - $5</div></div>
  <div class="item" style="left:465px;top:952px"><div class="item-name">Coffee - $5</div></div>
  <div class="item" style="left:465px;top:979px"><div class="item-name">Mineral Water - $5</div></div>
  <div class="item" style="left:465px;top:1006px"><div class="item-name">Orange Tundra - $5</div></div>
  <div class="item" style="left:465px;top:1033px"><div class="item-name">Blue Hawaii - $5</div></div>
  <div class="item" style="left:465px;top:1060px"><div class="item-name">Missouri Mule - $5</div></div>
  <div class="item" style="left:465px;top:1087px"><div class="item-name">Blue Hawaii - $5</div></div>
  <div class="item" style="left:465px;top:1113px"><div class="item-name">Missouri Mule - $5</div></div>

  <!-- Specials -->
  <aside>
    <div class="specials"></div>
    <div class="specials-band"></div>
    <h2 class="specials-title">SPECIALS</h2>

    <p class="special-name" style="top:395px">Salmon with avocado</p>
    <p class="special-desc" style="top:417px">Lorem ipsum dolor sit amet, consectetur adipiscing elit. Morbi egestas lacinia dolor eget elementum. Nunc consequat tortor sed ipsum tempus malesuada. Nunc</p>
    <div class="dish" style="left:636px;top:463px;width:138px;height:138px"><div class="photo" role="img" aria-label="Photo of tomato soup with bread" style="background:radial-gradient(circle,#c8603a,#6a5a4a)"></div></div>
    <div class="price" style="left:769px;top:499px">12$</div>

    <p class="special-name" style="top:618px">Salmon with avocado</p>
    <p class="special-desc" style="top:640px">Lorem ipsum dolor sit amet, consectetur adipiscing elit. Morbi egestas lacinia dolor eget elementum. Nunc</p>
    <p class="special-name" style="top:667px">Salmon with avocado</p>
    <p class="special-desc" style="top:689px">Lorem ipsum dolor sit amet, consectetur adipiscing elit. Morbi egestas lacinia dolor eget elementum. Nunc consequat tortor sed ipsum tempus malesuada. Nunc</p>
    <div class="dish" style="left:636px;top:729px;width:138px;height:138px"><div class="photo" role="img" aria-label="Photo of smoked salmon with avocado slices" style="background:radial-gradient(circle,#d98a62,#6f8a4a)"></div></div>
    <div class="price" style="left:769px;top:765px">12$</div>

    <p class="special-name" style="top:897px">Salmon with avocado</p>
    <p class="special-desc" style="top:919px">Lorem ipsum dolor sit amet, consectetur adipiscing elit. Morbi egestas lacinia dolor eget elementum. Nunc consequat tortor sed ipsum tempus malesuada. Nunc</p>
    <div class="dish" style="left:636px;top:969px;width:138px;height:138px"><div class="photo" role="img" aria-label="Photo of a toasted sandwich with a cup of coffee" style="background:radial-gradient(circle,#b58a5a,#5e5a40)"></div></div>
    <div class="price" style="left:769px;top:1005px">12$</div>
  </aside>
</main>
</body>
</html>
```